Minimalist Modern Business Card Design, open to ideas, or cleaner version of provided files, but what logo & logo colors (with some black) as shown in files, and info for back shown in files as well.

```html
<!DOCTYPE html>
<html lang="en">
<head>
<meta charset="utf-8">
<title>Northway Fleet Works – Business Card</title>
<link rel="stylesheet" href="https://fonts.googleapis.com/css2?family=Montserrat:wght@600&family=Archivo:wght@500;800&display=swap">
<style>
  :root {
    --navy: #25266a;
    --navy-deep: #212160;
    --navy-light: #2a2a74;
    --ink: #1a1a1a;
    --paper: #ffffff;
    --backdrop: #d3d4d6;
  }
  * { margin: 0; padding: 0; box-sizing: border-box; }
  html, body {
    width: 900px;
    height: 1200px;
    overflow: hidden;
    background: var(--backdrop);
  }
  .canvas { position: relative; width: 900px; height: 1200px; }

  .card {
    position: absolute;
    left: 134px;
    width: 632px;
    height: 362px;
  }
  .card--front {
    top: 212px;
    background: linear-gradient(100deg, var(--navy-deep) 0%, var(--navy) 50%, var(--navy-light) 100%);
  }
  .card--back {
    top: 628px;
    background: var(--paper);
  }

  .brand {
    position: absolute;
    display: flex;
    align-items: center;
    font-family: "Montserrat", sans-serif;
    font-weight: 600;
  }
  .brand__square { flex: none; }
  .brand__name { line-height: 1.05; }

  .card--front .brand { left: 133px; top: 138px; gap: 38px; color: var(--paper); }
  .card--front .brand__square { width: 86px; height: 86px; background: var(--paper); }
  .card--front .brand__name { font-size: 43px; }

  .card--back .brand { left: 53px; top: 152px; gap: 32px; color: var(--navy); }
  .card--back .brand__square { width: 54px; height: 54px; background: var(--navy); }
  .card--back .brand__name { font-size: 27px; }

  .divider {
    position: absolute;
    left: 315px;
    top: 112px;
    width: 2px;
    height: 136px;
    background: var(--ink);
  }

  .contact {
    position: absolute;
    left: 349px;
    top: 119px;
    font-family: "Archivo", sans-serif;
    color: var(--ink);
  }
  .contact__name {
    font-weight: 800;
    font-size: 23px;
    color: var(--navy);
    letter-spacing: 0.3px;
    line-height: 1;
  }
  .contact__role {
    margin-top: 6px;
    font-weight: 500;
    font-size: 13.5px;
    letter-spacing: 0.6px;
  }
  .contact__list { list-style: none; margin-top: 35px; }
  .contact__item {
    display: flex;
    align-items: center;
    gap: 6px;
    font-weight: 500;
    font-size: 13.5px;
    height: 26px;
  }
  .contact__item--phone { letter-spacing: 3px; }
  .contact__item--email { letter-spacing: 0.7px; }
  .icon { width: 14px; height: 14px; fill: var(--navy); flex: none; }
</style>
</head>
<body>
<div class="canvas">

  <section class="card card--front" aria-label="Card front">
    <div class="brand">
      <span class="brand__square" aria-hidden="true"></span>
      <span class="brand__name">Northway<br>Fleet Works</span>
    </div>
  </section>

  <section class="card card--back" aria-label="Card back">
    <div class="brand">
      <span class="brand__square" aria-hidden="true"></span>
      <span class="brand__name">Northway<br>Fleet Works</span>
    </div>

    <span class="divider" aria-hidden="true"></span>

    <div class="contact">
      <p class="contact__name">MY NAME</p>
      <p class="contact__role">President</p>
      <ul class="contact__list">
        <li class="contact__item contact__item--phone">
          <svg class="icon" viewBox="0 0 14 14" aria-hidden="true">
            <path d="M3 0h8v14H3z M4.2 1.5v9.5h5.6V1.5z M6.3 12h1.4v1H6.3z" fill-rule="evenodd"/>
          </svg>
          123-123-4567
        </li>
        <li class="contact__item contact__item--email">
          <svg class="icon" viewBox="0 0 14 14" aria-hidden="true">
            <path d="M0 3h14v1.2L7 8.3 0 4.2z M0 5.6l7 4.1 7-4.1V11H0z"/>
          </svg>
          xxxxxxx@xxxxxx.com
        </li>
      </ul>
    </div>
  </section>

</div>
</body>
</html>
```